Women's Online Clothing Boutique Needs Business Cards

I already have a logo that I would like to use. Some of the things that interest me is black business cards, foil embossed logo, glossy embossed logo, leopard print, no yellow font, rounded edges. I even like just a large logo on the front side with all of my information on the back side.

Contact Information for Business Card

https://silverheron.shopvenlo.com/
https://www.pagelink.net/thesilverheronboutique/
https://www.picfeed.net/thesilverheronboutique/
silverheronboutique@mailora.net

Requirements
Must have
• My Logo
Nice to have
• Leopard Print
Should not have
• No Yellow Font

```html
<!DOCTYPE html>
<html lang="en">
<head>
<meta charset="utf-8">
<title>The Silver Heron Boutique – Business Cards</title>
<link href="https://fonts.googleapis.com/css2?family=Roboto+Condensed:wght@300;400&display=swap" rel="stylesheet">
<style>
  :root {
    --bg-top: #3a3a3a;
    --bg-bottom: #141414;
    --card: #1e1e1e;
    --card-edge: #2a2a2a;
    --pattern: #262626;
    --gold: #c9a24a;
    --gold-light: #e8c870;
    --text: #e6e6e6;
  }
  * { margin: 0; padding: 0; box-sizing: border-box; }
  html, body { width: 1200px; height: 900px; overflow: hidden; }
  body {
    background: radial-gradient(ellipse at 50% 30%, var(--bg-top), var(--bg-bottom) 75%);
    font-family: "Roboto Condensed", "Arial Narrow", sans-serif;
    position: relative;
  }
  .card {
    position: absolute;
    width: 620px;
    height: 354px;
    border-radius: 28px;
    background: var(--card);
    box-shadow: 0 18px 40px rgba(0,0,0,.55), inset 0 0 0 1px var(--card-edge);
    overflow: hidden;
  }
  .card--back { left: 500px; top: 60px; }
  .card--front { left: 80px; top: 470px; }

  .pattern-fill {
    position: absolute; inset: 0;
    background: linear-gradient(135deg, var(--pattern), var(--card) 60%, var(--pattern));
  }

  .brand {
    position: absolute;
    left: 50%; top: 50%;
    transform: translate(-50%, -50%);
    display: flex; align-items: center; gap: 14px;
    white-space: nowrap;
  }
  .brand__mark {
    width: 34px; height: 34px; border-radius: 50%;
    background: var(--gold);
  }
  .brand__name {
    color: var(--gold);
    font-weight: 300;
    font-size: 40px;
    letter-spacing: 1px;
  }
  .rule {
    position: absolute; height: 1px;
    background: linear-gradient(90deg, transparent, var(--gold), transparent);
  }
  .card--back .rule--top { left: 150px; right: 150px; top: 130px; }
  .card--back .rule--bottom { left: 150px; right: 150px; top: 224px; }

  .socials {
    position: absolute; left: 40px; top: 30px;
    list-style: none;
  }
  .contact-line {
    display: flex; align-items: center; gap: 10px;
    color: var(--text); font-size: 17px; font-weight: 400;
    line-height: 26px; letter-spacing: .3px;
  }
  .icon {
    width: 16px; height: 16px; border-radius: 50%;
    background: var(--gold); flex: none;
    display: flex; align-items: center; justify-content: center;
  }
  .card--front .rule--divider {
    left: 40px; right: 40px; top: 96px;
    background: var(--gold); opacity: .8;
  }
  .card--front .brand { top: 178px; }
  .card--front .rule--under { left: 150px; right: 150px; top: 222px; }
  .contacts {
    position: absolute; right: 40px; bottom: 28px;
    list-style: none;
  }
  .contacts .contact-line { justify-content: flex-end; }
</style>
</head>
<body>

  <section class="card card--back" aria-label="Card back">
    <div class="pattern-fill" role="img" aria-label="Subtle tone-on-tone repeating animal silhouette pattern"></div>
    <div class="rule rule--top"></div>
    <div class="brand">
      <span class="brand__mark"></span>
      <span class="brand__name">The Silver Heron Boutique</span>
    </div>
    <div class="rule rule--bottom"></div>
  </section>

  <section class="card card--front" aria-label="Card front">
    <ul class="socials">
      <li class="contact-line"><span class="icon"></span>thesilverheronboutique/</li>
      <li class="contact-line"><span class="icon"></span>thesilverheronboutique/</li>
    </ul>
    <div class="rule rule--divider"></div>
    <div class="brand">
      <span class="brand__mark"></span>
      <span class="brand__name">The Silver Heron Boutique</span>
    </div>
    <div class="rule rule--under"></div>
    <ul class="contacts">
      <li class="contact-line">silverheronboutique@mailora.net
        <span class="icon">
          <svg width="10" height="8" viewBox="0 0 10 8"><rect x=".5" y=".5" width="9" height="7" fill="none" stroke="#1e1e1e"/><path d="M.5 .5 5 4.5 9.5 .5" fill="none" stroke="#1e1e1e"/></svg>
        </span>
      </li>
      <li class="contact-line">silverheron.shopvenlo.com
        <span class="icon">
          <svg width="10" height="10" viewBox="0 0 10 10"><circle cx="5" cy="5" r="4.3" fill="none" stroke="#1e1e1e"/><ellipse cx="5" cy="5" rx="1.8" ry="4.3" fill="none" stroke="#1e1e1e"/><path d="M.7 5h8.6" stroke="#1e1e1e"/></svg>
        </span>
      </li>
    </ul>
  </section>

</body>
</html>
```